Business Card for Business consulting practice

Need a design for a consultant business card. Simple and elegant.
I need the following information on the card:
Logo: (see uploaded file)
Company name: Calmora Advisory Group
Name: Dana Weltrup
Title: Managing Director - Aerospace and Defence
Phone #: 514-268-3917
e-mail: dana.weltrup@calmora-example.com
Website: www.calmora-example.com
Tagline: Proposals Management and Capture support for complex procurements

```html
<!DOCTYPE html>
<html lang="en">
<head>
<meta charset="utf-8">
<title>Calmora Advisory Group – Business Card</title>
<link rel="stylesheet" href="https://fonts.googleapis.com/css2?family=Poppins:wght@400;500;600&display=swap">
<style>
  :root {
    --backdrop: #b3b9c0;
    --navy: #0d2b40;
    --card-navy: #072d42;
    --accent: #1592bf;
    --white: #ffffff;
  }
  * { margin: 0; padding: 0; box-sizing: border-box; }
  html, body { width: 1200px; height: 2226px; overflow: hidden; }
  body {
    background: var(--backdrop);
    font-family: "Poppins", sans-serif;
    position: relative;
  }
  .card {
    position: absolute;
    left: 196px;
    width: 810px;
    height: 462px;
    border-radius: 30px;
    overflow: hidden;
  }
  .card--front { top: 629px; background: var(--white); }
  .card--back { top: 1135px; background: var(--card-navy); }

  .brand-mark {
    position: absolute;
    left: 70px;
    top: 206px;
    display: flex;
    align-items: center;
    gap: 12px;
  }
  .brand-mark__dot {
    width: 34px; height: 34px;
    border-radius: 50%;
    background: var(--accent);
  }
  .brand-mark__name {
    font-weight: 600;
    font-size: 40px;
    color: var(--navy);
    letter-spacing: 0.5px;
  }
  .divider {
    position: absolute;
    left: 368px;
    top: 118px;
    width: 3px;
    height: 226px;
    background: var(--accent);
  }
  .contact {
    position: absolute;
    left: 438px;
    top: 112px;
    color: var(--navy);
  }
  .contact__name {
    font-weight: 600;
    font-size: 31px;
    letter-spacing: 1.5px;
    line-height: 1.2;
  }
  .contact__title {
    font-weight: 500;
    font-size: 19px;
    color: var(--accent);
    line-height: 1.2;
    margin-top: 4px;
  }
  .contact__sector {
    font-size: 15px;
    line-height: 1.2;
  }
  .contact__list { list-style: none; margin-top: 24px; }
  .contact__item {
    display: flex;
    align-items: center;
    gap: 12px;
    font-size: 18px;
    height: 28px;
    margin-bottom: 13px;
  }
  .contact__icon { width: 29px; height: 29px; flex: none; }
  .contact__web {
    margin-top: 18px;
    font-weight: 600;
    font-size: 19px;
    letter-spacing: 1.5px;
    color: var(--accent);
  }

  .back__name {
    position: absolute;
    left: 0; right: 0;
    top: 168px;
    text-align: center;
    font-weight: 500;
    font-size: 46px;
    color: var(--white);
    letter-spacing: 1px;
  }
  .back__tagline {
    position: absolute;
    left: 0; right: 0;
    top: 372px;
    text-align: center;
    font-size: 22px;
    line-height: 1.25;
    color: var(--white);
  }
</style>
</head>
<body>
  <section class="card card--front">
    <div class="brand-mark">
      <span class="brand-mark__dot"></span>
      <span class="brand-mark__name">Calmora</span>
    </div>
    <div class="divider"></div>
    <div class="contact">
      <h1 class="contact__name">DANA WELTRUP</h1>
      <p class="contact__title">MANAGING DIRECTOR</p>
      <p class="contact__sector">Aerospace and Defence</p>
      <ul class="contact__list">
        <li class="contact__item">
          <svg class="contact__icon" viewBox="0 0 30 30" aria-hidden="true">
            <circle cx="15" cy="15" r="15" fill="var(--accent)"/>
            <path d="M10.5 8.5c.6-.6 1.5-.5 2 .1l1.5 2c.4.6.3 1.3-.2 1.8l-.9.8c.6 1.6 1.9 3 3.5 3.6l.8-.9c.5-.5 1.2-.6 1.8-.2l2 1.5c.6.5.7 1.4.1 2l-1 1c-.9.9-2.3 1.1-3.5.6-3.3-1.4-5.8-3.9-7.2-7.2-.5-1.2-.3-2.6.6-3.5z" fill="var(--white)"/>
          </svg>
          <span>514-268-3917</span>
        </li>
        <li class="contact__item">
          <svg class="contact__icon" viewBox="0 0 30 30" aria-hidden="true">
            <circle cx="15" cy="15" r="15" fill="var(--accent)"/>
            <rect x="8" y="10" width="14" height="10" rx="1.5" fill="var(--white)"/>
            <path d="M8.5 10.8 15 15.6l6.5-4.8" fill="none" stroke="var(--accent)" stroke-width="1.5"/>
          </svg>
          <span>dana.weltrup@calmora-example.com</span>
        </li>
      </ul>
      <p class="contact__web">WWW.CALMORA-EXAMPLE.COM</p>
    </div>
  </section>

  <section class="card card--back">
    <h2 class="back__name">Calmora Advisory Group</h2>
    <p class="back__tagline">Proposals Management and Capture<br>support for complex procurements</p>
  </section>
</body>
</html>
```